Banner Design Project

I need a banner designed that will be used in an outdoor location. The banner is 8' x 3' and can be full color.

This is a general advertising banner for a photography business; I can provide images if needed;

My website is: www.darvomkellphotography.com

It will be used at the following school: http://www.qbtrm.com/

Target Market(s)

All ages but should appeal to High School Students

Industry/Entity Type

Advertising

Requirements
Must have
• Integrate Logo

```html
<!DOCTYPE html>
<html lang="en">
<head>
<meta charset="utf-8">
<title>Darvom Kell Photography Banner</title>
<link rel="stylesheet" href="https://fonts.googleapis.com/css2?family=Jost:wght@400;500&display=swap">
<style>
  :root {
    --sky: #6cb4e4;
    --navy: #0b4a8b;
    --white: #ffffff;
    --face-red: #d9372c;
    --face-deep: #b82a22;
    --skin: #f1d2c2;
  }
  html, body {
    margin: 0;
    padding: 0;
    overflow: hidden;
    background: var(--white);
  }
  .banner {
    position: relative;
    width: 1200px;
    height: 450px;
    overflow: hidden;
    background: var(--white);
    font-family: "Jost", "Futura", sans-serif;
    color: var(--navy);
  }
  .brand {
    position: absolute;
    left: 58px;
    top: 30px;
    width: 772px;
    display: flex;
    align-items: center;
    gap: 22px;
    color: var(--navy);
    font-weight: 500;
  }
  .brand-mark {
    width: 22px;
    height: 22px;
    background: var(--navy);
    flex: none;
  }
  .brand-name {
    margin: 0;
    font-size: 58px;
    line-height: 1;
    letter-spacing: 0.42em;
    font-weight: 500;
    white-space: nowrap;
  }
  .brand-sub {
    position: absolute;
    right: 0;
    top: 92px;
    font-size: 21px;
    letter-spacing: 0.36em;
    font-weight: 500;
  }
  .services {
    position: absolute;
    left: 58px;
    top: 172px;
    display: grid;
    grid-template-columns: 292px 295px 200px;
    grid-auto-rows: 31px;
    grid-auto-flow: column;
    grid-template-rows: repeat(4, 31px);
    margin: 0;
    padding: 0;
    list-style: none;
  }
  .service {
    font-size: 25px;
    line-height: 31px;
    letter-spacing: 0.08em;
    font-weight: 500;
    white-space: nowrap;
  }
  .service::before {
    content: "";
    display: inline-block;
    width: 7px;
    height: 7px;
    border-radius: 50%;
    background: var(--sky);
    margin-right: 8px;
    vertical-align: 6px;
  }
  .contact-call {
    position: absolute;
    left: 0;
    width: 890px;
    top: 316px;
    text-align: center;
    font-size: 41px;
    line-height: 1;
    font-weight: 500;
    margin: 0;
  }
  .contact-web {
    position: absolute;
    left: 0;
    width: 890px;
    top: 377px;
    text-align: center;
    font-size: 41px;
    line-height: 1;
    font-weight: 500;
    margin: 0;
  }
  .soft { color: var(--sky); }
  .strong { color: var(--navy); }
  .portrait {
    position: absolute;
    left: 880px;
    top: 0;
    width: 320px;
    height: 450px;
  }
</style>
</head>
<body>
  <div class="banner">
    <header class="brand">
      <span class="brand-mark"></span>
      <h1 class="brand-name">DARVOM KELL</h1>
      <span class="brand-sub">PHOTOGRAPHY</span>
    </header>

    <ul class="services">
      <li class="service">PORTRAITURE</li>
      <li class="service">FAMILY</li>
      <li class="service">COUPLES</li>
      <li class="service">WEDDING</li>
      <li class="service">ENGAGEMENTS</li>
      <li class="service">WATER</li>
      <li class="service">SURFING</li>
      <li class="service">SPORTS</li>
      <li class="service">ACTION</li>
      <li class="service">EVENTS</li>
      <li class="service">PARTIES</li>
      <li class="service">CORPORATE</li>
    </ul>

    <p class="contact-call"><span class="soft">Call</span> <span class="strong">00 1 555 204 7736</span></p>
    <p class="contact-web"><span class="soft">www.</span><span class="strong">darvomkellphotography</span><span class="soft">.com</span></p>

    <svg class="portrait" viewBox="0 0 320 450" role="img" aria-label="Close-up photograph of a young person with red face paint and dark web pattern">
      <defs>
        <linearGradient id="portrait-tone" x1="0" y1="0" x2="1" y2="0">
          <stop offset="0" stop-color="#ffffff"/>
          <stop offset="0.12" stop-color="#f1d2c2"/>
          <stop offset="0.35" stop-color="#d9372c"/>
          <stop offset="1" stop-color="#b82a22"/>
        </linearGradient>
      </defs>
      <rect width="320" height="450" fill="url(#portrait-tone)"/>
    </svg>
  </div>
</body>
</html>
```